Homeopathic medicinal cream label design

I am looking for a product label design for a medicinal (cannabis) topical cream to be sold to medical marijuana patients. It is a new product that has not yet established a brand identity. It will be sold in 2 and 4 ounce containers so the design needs to work on a small scale. The design may be used for other branding as well.

Target Market(s)

Medical marijuana users in states where it is legal. The product should appeal to both men and women to promote pain relief in muscles and joints. It can also be used as a massage cream for general relaxation.

Industry/Entity Type

Medical

Font styles to use
Sans Serif

Requirements
Must have
• Something that reflects the company name - The Quiet Lark - and the name of the initial product - Meadow Balm Blend.
• In addition to the name of the company and the name of the product, other information to include would be the volume being sold (e.g. 4 oz.), that it is a topical botanical ointment, and its ingredients (coconut oil, beeswax, soy lecithin, and eight all natural botanical oils - cannabis, lavender, eucalyptus, peppermint, rosemary, cinnamon, clove, and lemon). The label should clearly state that the product is for topical use only.
• The information must fit on the space available on the package. The 4 oz. container's lid has approximately 2 1/8" of surface area. The width of the label on the lid should be approximately 1 7/8". On the container's body, the height of the surface area is approximately 1", and the width is approximately 8 1/2 inches. The width of the label should be around 8 inches to allow room for it to be applied to the container. I have posted a photo of the 4 oz. container and the 2 oz. container. I have also posted a photo of the labeling of some of our competitors with similar products.
Nice to have
• We are thinking of having the logo on the lid of the container, and a circle bordering the lid that may have text in it. (See the "Amber Owl" label attached as an exemplar).
• The label on the body of the container (or maybe on the bottom on the container) would list other information about the product, such as its ingredients and our contact information.

```html
<!DOCTYPE html>
<html lang="en">
<head>
<meta charset="utf-8">
<title>Meadow Balm Blend — Label Set</title>
<link rel="stylesheet" href="https://fonts.googleapis.com/css2?family=Jost:wght@400;500;600;800&family=Source+Sans+3:wght@400;700&display=swap">
<style>
  :root {
    --canvas: #ffffff;
    --card: #ffffff;
    --leaf-green: #a4c13a;
    --leaf-shade: #7f9a4c;
    --ink: #5c5a5e;
    --seal-inner: #eaf0d6;
    --placeholder-light: #f4f6ee;
    --shadow: rgba(0, 0, 0, 0.28);
  }
  * { box-sizing: border-box; margin: 0; padding: 0; }
  html, body {
    width: 1030px;
    height: 1200px;
    overflow: hidden;
    background: var(--canvas);
  }
  .canvas {
    position: relative;
    width: 1030px;
    height: 1200px;
  }
  .label-card {
    position: absolute;
    left: 36px;
    width: 956px;
    background: var(--card);
    box-shadow: 0 2px 8px var(--shadow);
    overflow: visible;
  }
  .label-card--body { top: 25px; height: 360px; }
  .label-card--back { top: 410px; height: 362px; }

  .body-band {
    position: absolute;
    left: 28px;
    top: 52px;
    width: 896px;
    height: 251px;
    background: var(--leaf-green);
  }
  .leaf-mark {
    position: absolute;
    background: var(--leaf-shade);
    opacity: 0.55;
    border-radius: 50% 50% 46% 46%;
  }
  .leaf-mark--front { left: 613px; top: 20px; width: 311px; height: 319px; }
  .leaf-mark--back { left: 32px; top: 34px; width: 283px; height: 292px; opacity: 0.4; }

  .mascot-art {
    position: absolute;
    left: 37px;
    top: 71px;
    width: 237px;
    height: 203px;
    background: linear-gradient(160deg, #ffffff 0%, #eef2e2 70%, #c9cfbf 100%);
    border-radius: 40% 40% 30% 30%;
    opacity: 0.9;
  }
  .product-title {
    position: absolute;
    right: 54px;
    top: 130px;
    font-family: "Jost", "Futura", sans-serif;
    font-weight: 800;
    font-size: 60px;
    line-height: 1;
    letter-spacing: 1.5px;
    color: var(--ink);
    white-space: nowrap;
  }
  .product-subtitle {
    position: absolute;
    left: 355px;
    top: 193px;
    font-family: "Jost", "Futura", sans-serif;
    font-weight: 600;
    font-size: 29px;
    line-height: 1;
    color: var(--ink);
    white-space: nowrap;
  }

  .ingredients-panel {
    position: absolute;
    left: 32px;
    top: 63px;
    width: 461px;
    height: 230px;
    background: var(--leaf-green);
  }
  .ingredients-copy {
    position: absolute;
    left: 32px;
    top: 63px;
    width: 461px;
    padding: 18px 38px 0;
    font-family: "Source Sans 3", "Myriad Pro", sans-serif;
    font-size: 21px;
    line-height: 26px;
    color: var(--ink);
    text-align: justify;
    text-align-last: center;
  }
  .ingredients-copy strong { font-weight: 700; }
  .usage-note {
    margin-top: 10px;
    font-weight: 700;
    font-size: 19px;
    text-align: center;
    text-align-last: center;
  }
  .net-volume {
    margin-top: 4px;
    font-weight: 700;
    font-size: 18px;
    text-align: center;
    text-align-last: center;
  }

  .lid-seal {
    position: absolute;
    left: 574px;
    top: 21px;
    width: 316px;
    height: 316px;
  }
  .seal-ring-text {
    font-family: "Jost", "Century Gothic", sans-serif;
    font-weight: 500;
    font-size: 21px;
    fill: #ffffff;
  }
  .seal-name {
    font-family: "Jost", "Century Gothic", sans-serif;
    font-weight: 400;
    font-size: 25px;
    fill: #2f2e30;
  }
  .seal-volume {
    font-family: "Source Sans 3", sans-serif;
    font-weight: 700;
    font-size: 11px;
    fill: var(--ink);
  }
</style>
</head>
<body>
<main class="canvas">

  <section class="label-card label-card--body" aria-label="Container body label">
    <div class="body-band"></div>
    <div class="leaf-mark leaf-mark--front" role="img" aria-label="Large faint botanical leaf illustration"></div>
    <div class="mascot-art" role="img" aria-label="Illustrated mascot walking on a curved line"></div>
    <h1 class="product-title">MEADOW BALM BLEND</h1>
    <p class="product-subtitle">topical botanical ointment</p>
  </section>

  <section class="label-card label-card--back" aria-label="Ingredients label and lid label">
    <div class="ingredients-panel"></div>
    <div class="leaf-mark leaf-mark--back" role="img" aria-label="Faint botanical leaf illustration"></div>
    <div class="ingredients-copy">
      <p><strong>ingredients</strong>: coconut oil, beeswax, soy lecithin, and eight all natural botanical oils - cannabis, lavender, eucalyptus, peppermint, rosemary, cinnamon, clove, and lemon.</p>
      <p class="usage-note">TOPICAL USE ONLY</p>
      <p class="net-volume">4 oz.</p>
    </div>

    <svg class="lid-seal" viewBox="0 0 316 316" aria-label="Lid label">
      <defs>
        <path id="seal-ring-path" d="M 32,158 A 126 126 0 1 1 284,158 A 126 126 0 1 1 32,158"/>
      </defs>
      <circle cx="158" cy="158" r="156" fill="var(--leaf-green)"/>
      <circle cx="158" cy="158" r="111" fill="var(--seal-inner)"/>
      <text class="seal-ring-text">
        <textPath href="#seal-ring-path" textLength="770" lengthAdjust="spacing">topical botanical ointment • meadow balm blend • cannabis topical cream •</textPath>
      </text>
      <rect x="98" y="78" width="120" height="86" rx="30" fill="var(--placeholder-light)" stroke="#d9dfca" role="img" aria-label="Mascot illustration"/>
      <text class="seal-name" x="158" y="200" text-anchor="middle">the quiet lark</text>
      <text class="seal-volume" x="158" y="228" text-anchor="middle">4 oz.</text>
    </svg>
  </section>

</main>
</body>
</html>
```